Design a beautiful book cover for my self help book

The Craft of Hush is a book I've written about how I learnt to quite my mind, rid myself of old pain and stand in my intuition. It's one simple practical tool to find you moment and step into your abundance. We need a cover that reflects this amazing concept! The current cover is attached. It's too dark and not in tune with the market. Please search books with similar content and make design similar yet different.

Target Market(s)

People into self help or motivational content. As well as people suffering from depression, stress, anxiety etc.

Industry/Entity Type

Self Help

Requirements
Must have
• A light airy feel of freedom
Nice to have
• Some sort of linage from current cover
Should not have
• Dark, ambiguous,

```html
<!DOCTYPE html>
<html lang="en">
<head>
<meta charset="utf-8">
<title>The Craft of Hush — Book Cover</title>
<link rel="stylesheet" href="https://fonts.googleapis.com/css2?family=Cormorant+Garamond:wght@500;600&family=Jost:wght@400&display=swap">
<style>
  :root {
    --page: #ffffff;
    --sky-top: #cfdfe4;
    --sky-mid: #e9ece6;
    --cream: #f6f1e7;
    --haze: #ece8dc;
    --ink: #416877;
    --ink-soft: #4d6f7d;
    --bird-light: #dfe8ea;
    --bird-mid: #a9c0c8;
  }
  * { margin: 0; padding: 0; box-sizing: border-box; }
  html, body {
    width: 1200px; height: 1200px; overflow: hidden;
    background: var(--page);
  }
  .book-cover {
    position: absolute;
    left: 236px; top: 52px;
    width: 735px; height: 1102px;
    background:
      radial-gradient(ellipse 60% 18% at 30% 14%, rgba(255,255,255,0.55), transparent 70%),
      radial-gradient(ellipse 50% 14% at 80% 22%, rgba(255,255,255,0.45), transparent 70%),
      linear-gradient(180deg, var(--sky-top) 0%, var(--sky-mid) 28%, var(--cream) 55%, var(--cream) 80%, var(--haze) 100%);
    overflow: hidden;
  }
  .title {
    position: absolute; left: 0; width: 100%;
    text-align: center;
    font-family: "Cormorant Garamond", serif;
    font-weight: 600;
    color: var(--ink);
    line-height: 1;
  }
  .title-the  { top: 140px; font-size: 78px; letter-spacing: 6px; }
  .title-craft { top: 236px; font-size: 118px; letter-spacing: 2px; }
  .title-hush { top: 380px; font-size: 150px; letter-spacing: 8px; }
  .bird-illustration {
    position: absolute;
    left: 250px; top: 540px;
    width: 330px; height: 165px;
    border-radius: 50%;
    background: radial-gradient(ellipse at 45% 50%, var(--bird-mid) 0%, var(--bird-light) 45%, rgba(246,241,231,0) 72%);
  }
  .subtitle {
    position: absolute; left: 0; top: 742px; width: 100%;
    text-align: center;
    font-family: "Jost", sans-serif;
    font-weight: 400;
    font-size: 26px;
    line-height: 45px;
    letter-spacing: 0.5px;
    color: var(--ink-soft);
  }
  .author {
    position: absolute; left: 0; top: 962px; width: 100%;
    text-align: center;
    font-family: "Cormorant Garamond", serif;
    font-weight: 500;
    font-size: 56px;
    letter-spacing: 9px;
    line-height: 1;
    color: var(--ink);
  }
</style>
</head>
<body>
  <main class="book-cover">
    <h1>
      <span class="title title-the">THE</span>
      <span class="title title-craft">CRAFT OF</span>
      <span class="title title-hush">HUSH</span>
    </h1>
    <div class="bird-illustration" role="img" aria-label="Soft watercolour bird in flight with three small birds in the distance"></div>
    <p class="subtitle">
      How I Learned to Quiet My Mind,<br>
      Rid Myself of Old Pain, and<br>
      Stand in My Intuition
    </p>
    <p class="author">BRODY LANE</p>
  </main>
</body>
</html>
```